lumaVex Sports - Cycling Headphones

Looking for a set of web banners for a product we're bringing to the Australian market:
lumaVex Sports are in-ear headphones designed to provide the wearer with total sound awareness; which obviously makes listening to music or podcasts a lot safer for cyclists.

You can get a full run down on the product over at http://www.lumaVexSports.com.au

The banners will be tested across the web, and also provided to our affiliate partners to use in their promotions.

Tag Lines can include:
Cycle Safer
Total Sound awareness
Worlds Safest Headphones
Originally designed for NRQ + DLT
(or feel free to get creative)

Please also include a strong call to action button to elicit response. Something like [Order Today] [Find Our Mote] [Click Here To Cycle Safer] etc etc

Target Market(s)

Cyclists: Generally 30-55 years old.

Industry/Entity Type

Affiliate

Font styles to use
Serif
Sans Serif

Requirements
Must have
• Call to Action Button.
• Image of Cyclist and/or product
• Tagline of some description.

```html
<!DOCTYPE html>
<html lang="en">
<head>
<meta charset="utf-8">
<title>lumaVex Sports – Total Sound Awareness Banner</title>
<link rel="stylesheet" href="https://fonts.googleapis.com/css2?family=Questrial&family=Oswald:wght@500&family=Roboto:wght@700&display=swap">
<style>
  :root {
    --page-bg: #1b1b1b;
    --photo-top: #3a3d40;
    --photo-mid: #8c8e8c;
    --photo-low: #6b6a55;
    --photo-base: #9a9790;
    --ink-dark: #151515;
    --ink-light: #ffffff;
    --band: rgba(20, 20, 20, 0.72);
    --corner: #2a2a2a;
    --product-dark: #141414;
    --product-grey: #5a5c5c;
  }
  * { margin: 0; padding: 0; box-sizing: border-box; }
  html, body { width: 1200px; height: 900px; overflow: hidden; }
  body { background: var(--page-bg); position: relative; }

  .banner {
    position: absolute;
    left: 20px; top: 226px;
    width: 1158px; height: 428px;
    overflow: hidden;
  }
  .banner__photo {
    position: absolute; inset: 0;
    background:
      radial-gradient(ellipse 260px 200px at 380px 200px, rgba(120,80,70,0.45), transparent 70%),
      radial-gradient(ellipse 420px 160px at 200px 120px, rgba(200,200,200,0.5), transparent 70%),
      linear-gradient(180deg, var(--photo-top) 0%, var(--photo-mid) 38%, var(--photo-low) 68%, var(--photo-base) 100%);
  }
  .offer-corner { position: absolute; left: 0; top: 0; width: 70px; height: 70px; }

  .headline {
    position: absolute; left: 14px; top: 113px;
    padding: 2px 6px 0 4px;
    background: linear-gradient(90deg, var(--band), rgba(20,20,20,0.35));
    font-family: "Questrial", sans-serif;
    font-size: 35px; line-height: 38px;
    color: var(--ink-light);
    letter-spacing: 0.5px;
  }
  .subline {
    position: absolute; left: 313px; top: 155px;
    font-family: "Roboto", sans-serif; font-weight: 700;
    font-size: 13px; letter-spacing: 1px;
    color: var(--ink-light);
  }
  .ride-safer {
    position: absolute; left: 48px; top: 256px;
    width: 527px;
    padding-bottom: 6px;
    border-bottom: 1px solid rgba(20,20,20,0.6);
    font-family: "Questrial", sans-serif;
    font-size: 22px; letter-spacing: 5px;
    color: var(--ink-dark);
  }
  .order-button {
    position: absolute; left: 204px; top: 307px;
    width: 194px; height: 40px;
    background: linear-gradient(180deg, #2a2a2a, #050505);
    box-shadow: 0 2px 6px rgba(0,0,0,0.5);
    font-family: "Oswald", sans-serif; font-weight: 500;
    font-size: 26px; line-height: 40px; letter-spacing: 1px;
    color: var(--ink-light); text-align: center;
    text-decoration: none;
  }
  .product-shot {
    position: absolute; left: 648px; top: 22px;
    width: 452px; height: 388px;
    background: linear-gradient(90deg, var(--product-dark) 0%, var(--product-dark) 42%, var(--product-grey) 43%, #3f4141 100%);
  }
</style>
</head>
<body>
  <section class="banner" aria-label="lumaVex Sports cycling headphones banner">
    <div class="banner__photo" role="img" aria-label="Blurred photo of a cyclist riding outdoors"></div>

    <svg class="offer-corner" viewBox="0 0 70 70" aria-label="20% off">
      <polygon points="0,0 70,0 0,70" fill="var(--corner)"/>
      <text x="23" y="23" fill="#fff" font-family="Roboto, sans-serif" font-weight="700" font-size="13" text-anchor="middle" transform="rotate(-45 23 23)">
        <tspan x="23" dy="-2">20%</tspan><tspan x="23" dy="13">OFF</tspan>
      </text>
    </svg>

    <h1 class="headline">TOTAL SOUND AWARENESS</h1>
    <p class="subline">WORLDS SAFEST HEADPHONES</p>
    <p class="ride-safer">We want you to ride Safer.....</p>
    <a class="order-button" href="http://www.lumaVexSports.com.au">ORDER NOW</a>

    <div class="product-shot" role="img" aria-label="lumaVex Sports in-ear headphones in an open presentation box with case"></div>
  </section>
</body>
</html>
```